Bref créative
bluetidal business card
business card for bluetidal.example
Professional
Margaret Pellowin
General Manager
p.o.box 4872 - 519 Maplecrest Ct Nw
garnok77@mailzone.example
http://www.bluetidal.example/
bluetidal logo

```html
<!DOCTYPE html>
<html lang="en">
<head>
<meta charset="utf-8">
<title>bluetidal business card</title>
<link rel="stylesheet" href="https://fonts.googleapis.com/css2?family=Arimo:wght@400;700&display=swap">
<style>
  :root {
    --backdrop: #3a2418;
    --card: #ffffff;
    --ink: #111111;
    --brand-blue: #1c9ac7;
    --band-blue: #1a9cc4;
    --accent-orange: #e5592b;
  }
  * { margin: 0; padding: 0; box-sizing: border-box; }
  html, body {
    width: 1200px;
    height: 749px;
    overflow: hidden;
    background: var(--backdrop);
    font-family: "Arimo", Arial, sans-serif;
  }
  .card {
    position: absolute;
    left: 168px;
    top: 118px;
    width: 864px;
    height: 500px;
    background: var(--card);
    box-shadow: 0 6px 18px rgba(0,0,0,0.45);
  }
  .brand-name {
    position: absolute;
    left: 14px;
    top: 56px;
    font-weight: 700;
    font-size: 46px;
    line-height: 54px;
    color: var(--brand-blue);
  }
  .person {
    position: absolute;
    left: 552px;
    top: 54px;
    color: var(--ink);
  }
  .person-name {
    font-weight: 700;
    font-size: 27px;
    line-height: 32px;
  }
  .person-title {
    font-size: 24px;
    line-height: 30px;
  }
  .contact {
    position: absolute;
    left: 0;
    width: 100%;
    top: 354px;
    padding-left: 60px;
    text-align: center;
    font-size: 24px;
    line-height: 29px;
    color: var(--ink);
  }
  .stripe-orange {
    position: absolute;
    left: 0; width: 100%;
    top: 458px; height: 8px;
    background: var(--accent-orange);
  }
  .stripe-blue {
    position: absolute;
    left: 0; width: 100%;
    top: 472px; height: 22px;
    background: var(--band-blue);
  }
</style>
</head>
<body>
  <div class="card">
    <p class="brand-name">bluetidal</p>
    <div class="person">
      <p class="person-name">Margaret Pellowin</p>
      <p class="person-title">General Manager</p>
    </div>
    <div class="contact">
      <p>p.o.box 4872 - 519 Maplecrest Ct Nw</p>
      <p>Phone: 555-014-2387,Fax: 555-014-23920</p>
      <p>Email: garnok77@mailzone.example,http://www.bluetidal.example/</p>
    </div>
    <div class="stripe-orange"></div>
    <div class="stripe-blue"></div>
  </div>
</body>
</html>
```